UK Leading HighTech Tooling distributor letterhead

We are one of the UK's leading Engineering Tooling distributers, we are launching our great new catalogue in May and want a red-hot eye catching letterhead to accompany the catalogue.

We want customers who see it to think high quality and premium.

We will roll out the successful style of design accross our other marketing goods (bus cards, website, emails etc) so the winning design will gain more work as a result.

Finally - we are in a rush so please submit quickly your best designs!

Target Market(s)

Precision engineers, senior buyers and managing directors.

Industry/Entity Type

Marketing

Requirements
Must have
• It must feature the Brandor logo as the MAIN logo.
It must have a tag line of 'Complete Tooling Solutions' somewhere on the page.
It should feature our 6 supplier logo's as sub logo's

Contact details:
tel 01632 960417
fax 01632 960418
web brandorkit.co.uk
email sales@brandor.example
address : Brandor Ltd, Marsh Offices, Fennick Street, Carnford, West Marlshire, HX7 4QD, United Kingdom
Company registration 5718346
Vat no. 871 2043 58
Nice to have
• Bring our logo alive

I have attached an old version of our letterhead so you can see details - please make it much better!

```html
<!DOCTYPE html>
<html lang="en">
<head>
<meta charset="utf-8">
<title>Brandor Ltd – Letterhead</title>
<link href="https://fonts.googleapis.com/css2?family=Exo+2:wght@300&family=Noto+Sans:wght@400&family=PT+Sans:wght@400;700&display=swap" rel="stylesheet">
<style>
  :root {
    --backdrop: #e9ebee;
    --paper: #ffffff;
    --brand-blue: #2a8fc8;
    --brand-deep: #15558f;
    --brand-light: #5cc0d8;
    --ink: #1e1e1e;
    --muted: #555a60;
    --signature-tone: #eceef0;
    --partner-ink: #1d3f7a;
  }
  * { box-sizing: border-box; margin: 0; padding: 0; }
  html, body {
    width: 1042px; height: 1200px; overflow: hidden;
    background: var(--backdrop);
  }
  .letterhead {
    position: absolute; left: 57px; top: 0;
    width: 927px; height: 1200px;
    background: var(--paper);
    overflow: hidden;
  }
  .brand-mark {
    position: absolute; left: 39px; top: 78px;
    display: flex; align-items: center; gap: 12px;
    font-family: "PT Sans", sans-serif; font-weight: 700;
    font-size: 44px; color: var(--brand-blue); letter-spacing: 1px;
  }
  .brand-mark .dot {
    width: 46px; height: 46px; border-radius: 50%;
    background: var(--brand-blue);
  }
  .company-details {
    position: absolute; left: 407px; top: 67px;
    font-family: "PT Sans", sans-serif; font-size: 14px;
    line-height: 20px; color: var(--muted); font-style: normal;
  }
  .company-details .name,
  .company-details .label { color: var(--brand-blue); }
  .contact-list {
    position: absolute; left: 757px; top: 67px;
    list-style: none;
    font-family: "PT Sans", sans-serif; font-size: 14px;
    line-height: 20px; color: var(--muted);
  }
  .contact-list li { display: flex; align-items: center; gap: 6px; }
  .contact-list svg { width: 13px; height: 13px; fill: var(--brand-blue); }
  .letter-body {
    position: absolute; left: 126px; top: 322px; width: 676px;
    font-family: "Noto Sans", sans-serif; font-size: 13.6px;
    line-height: 18px; color: var(--ink);
    text-align: justify; hyphens: auto;
  }
  .letter-body p + p { margin-top: 18px; }
  .signature {
    position: absolute; left: 134px; top: 850px;
    width: 143px; height: 108px;
    background: var(--signature-tone); border-radius: 4px;
  }
  .partner-row {
    position: absolute; left: 81px; top: 1042px; width: 766px;
    display: flex; justify-content: space-between; align-items: center;
    font-family: "PT Sans", sans-serif; font-weight: 700;
    font-size: 20px; color: var(--partner-ink);
  }
  .footer-wave {
    position: absolute; left: 0; top: 1000px; width: 927px; height: 200px;
  }
  .tagline {
    position: absolute; left: 35px; top: 1158px;
    font-family: "Exo 2", sans-serif; font-weight: 300;
    font-size: 24px; color: #ffffff;
  }
</style>
</head>
<body>
<main class="letterhead">
  <div class="brand-mark"><span class="dot"></span><span>BRANDOR</span></div>

  <address class="company-details">
    <div class="name">Brandor Limited</div>
    <div>Marsh Offices, Fennick Street, Carnford,</div>
    <div>West Marlshire, HX7 4QD,&nbsp; United Kingdom,</div>
    <div><span class="label">Company registration</span> 5718346&nbsp; <span class="label">Vat No.</span> 871 2043 58</div>
  </address>

  <ul class="contact-list">
    <li><svg viewBox="0 0 16 16"><path d="M2 6c0-2 2-3 6-3s6 1 6 3l-3 1-1-2H6L5 7 2 6zm2 2h8l1 5H3z"/></svg>01632 960417</li>
    <li><svg viewBox="0 0 16 16"><path d="M4 1h8v4H4zM2 6h12v8H2zm2 2v2h8V8z"/></svg>01632 960418</li>
    <li><svg viewBox="0 0 16 16"><path d="M1 3h14v10H1zm1 1v1l6 4 6-4V4z"/></svg>sales@brandor.example</li>
    <li><svg viewBox="0 0 16 16"><path d="M8 1l7 7h-2v7H9v-4H7v4H3V8H1z"/></svg>brandorkit.co.uk</li>
  </ul>

  <section class="letter-body">
    <p>Lorem ipsum dolor sit amet, consectetuer adipiscing elit. Pellentesque tristique elementum sem. Quisque eget erat ac lectus sodales faucibus. Nam commodo est. Cras consequat faucibus velit. Nam ac magna. Sed et ligula. Nam volutpat, elit ac facilisis tempor, neque augue euismod leo, sit amet molestie sem est eu libero. Nulla facilisi. Pellentesque sit amet odio. Curabitur a leo consectetuer leo blandit porttitor. Pellentesque velit quam, gravida at, pharetra eu, convallis non, sem. Aenean tempor nibh at purus. Pellentesque porta. Suspendisse congue, lacus sit amet imperdiet imperdiet, urna massa rutrum urna, id elementum tellus diam quis risus.</p>
    <p>In dui turpis, varius vitae, tincidunt id, consequat ut, leo. Donec tincidunt tristique odio. Nulla erat felis, euismod nec, fringilla non, aliquet et, magna. Nulla at magna quis nisi pretium vehicula. Pellentesque habitant morbi tristique senectus et netus et malesuada fames ac turpis egestas. Class aptent taciti sociosqu ad litora torquent per conubia nostra, per inceptos himenaeos. In vel quam. Phasellus varius convallis purus. In non turpis. Nam sed risus. Etiam non neque at nisl gravida porttitor. Donec leo dolor, feugiat ut, pharetra et, porttitor a, metus. Suspendisse laoreet magna vel elit. Ut est augue, fermentum ac, molestie at, vestibulum et, urna.</p>
    <p>Nunc purus. Cras auctor. In ornare neque id ipsum. Nulla tincidunt, diam sit amet viverra euismod, sapien augue fringilla neque, at pellentesque felis tortor vel enim. Etiam dignissim. Sed a tortor vel nisl euismod ultricies. Donec molestie congue lectus. Integer sed turpis a tortor imperdiet consequat. Maecenas molestie placerat urna. Sed pede enim, sollicitudin nec, pretium nec, sollicitudin a, felis. In hac habitasse platea dictumst. Nam facilisis, tellus non scelerisque placerat, turpis turpis semper ante, euismod imperdiet augue nisi et neque. Vivamus tincidunt.</p>
    <p>Nulla lobortis ultricies nulla. Pellentesque purus mi, consequat quis, hendrerit sed, imperdiet non, eros. Nullam urna est, vehicula nec, cursus nec, dignissim sit amet, risus. Duis molestie, tellus sit amet laoreet ullamcorper, urna nisi fringilla ante, at rhoncus justo dolor vel dui. Nam hendrerit luctus lorem. Aenean tempor, metus vel posuere gravida, arcu nunc imperdiet tellus, ut blandit sem magna a turpis. Vivamus in neque. Lorem ipsum dolor sit amet consectetuer adipiscing.</p>
  </section>

  <div class="signature" role="img" aria-label="Handwritten signature"></div>

  <div class="partner-row">
    <span>Vantor</span>
    <span>Halden Inc.</span>
    <span>Morelli</span>
    <span>Kestrel</span>
    <span>Ardent Inc.</span>
    <span>Tremark</span>
  </div>

  <svg class="footer-wave" viewBox="0 0 927 200" preserveAspectRatio="none" aria-hidden="true">
    <defs>
      <linearGradient id="band" x1="0" y1="0" x2="1" y2="0">
        <stop offset="0" stop-color="#1f72b4"/>
        <stop offset="0.45" stop-color="#5cc0d8"/>
        <stop offset="1" stop-color="#1c74b3"/>
      </linearGradient>
      <linearGradient id="ribbon" x1="0" y1="0" x2="1" y2="0">
        <stop offset="0" stop-color="#ffffff" stop-opacity="0"/>
        <stop offset="0.6" stop-color="#bfe4f1"/>
        <stop offset="1" stop-color="#2a8fc8"/>
      </linearGradient>
    </defs>
    <path d="M0 148 C 200 120 420 150 560 156 C 720 160 840 120 927 95 L927 200 L0 200 Z" fill="url(#band)"/>
    <path d="M0 142 C 200 100 420 140 560 146 C 720 150 840 110 927 88 L927 95 C 840 120 720 160 560 156 C 420 150 200 120 0 148 Z" fill="url(#ribbon)"/>
    <path d="M0 130 C 140 104 260 104 400 126 C 500 142 600 146 700 128 C 800 110 870 92 927 80" fill="none" stroke="var(--brand-deep)" stroke-width="3"/>
  </svg>

  <div class="tagline">Complete Tooling Solutions</div>
</main>
</body>
</html>
```